Flyer für Reifen- und Autoservicebetrieb
Zielgruppe
Wir sind ein Reifen- und Autoservicebetrieb; eine freie KFZ-Meister-Werkstatt ohne Markenbindung.
Aufgabenstellung
Im Focus des Flyers soll auf der Vorderseite der Reifenservice stehen, da dieser zur bevorstehenden Winterreifen-Wechselsaison erscheinen wird (Reifenwechsel, Einlagerung, Räderwäsche, Online-Termin). Auf der Rückseite soll der Autoservice und der 'neu' angebotene LKW- und Landwirtschafts- Reifenservice beworben werden.

```html
<!DOCTYPE html>
<html lang="de">
<head>
<meta charset="utf-8">
<title>Vorland Reifen – Flyer</title>
<link href="https://fonts.googleapis.com/css2?family=Barlow:wght@300;400;500;600;700;800&family=Barlow+Condensed:wght@300;700;800&display=swap" rel="stylesheet">
<style>
:root{
  --orange:#f19d2a;
  --dark:#323233;
  --ink:#2b2b2c;
  --paper:#f7f7f7;
  --stage:#77777a;
  --line:#cfcfcf;
}
*{box-sizing:border-box;margin:0;padding:0}
html,body{width:873px;height:1200px;overflow:hidden}
body{background:var(--stage);font-family:"Barlow",sans-serif;color:var(--ink);position:relative}
.flyer{position:absolute;top:317px;width:400px;height:566px;background:var(--paper);overflow:hidden;box-shadow:0 8px 18px rgba(0,0,0,.35)}
.flyer--front{left:24px}
.flyer--back{left:449px}

/* front */
.hero-photo{position:absolute;left:0;top:60px;width:400px;height:290px;
  background:linear-gradient(180deg,rgba(247,247,247,1) 0%,rgba(214,220,228,.9) 30%,#a9b3c1 55%,#d9dde3 80%,rgba(247,247,247,1) 100%)}
.accent-block{position:absolute;left:232px;top:122px;width:106px;height:137px;background:var(--orange)}
.tyre-photo{position:absolute;left:80px;top:142px;width:220px;height:175px;border-radius:40px;
  background:radial-gradient(ellipse at 50% 50%,#7d8085 0%,#3a3b3e 45%,#1d1d1f 70%,rgba(29,29,31,0) 72%)}
.brand{position:absolute;right:10px;top:22px;display:flex;align-items:center;gap:5px;font-weight:600;font-size:12px;color:var(--orange);letter-spacing:.3px}
.brand__dot{width:10px;height:10px;border-radius:50%;background:#8a8a8c}
.booking-note{position:absolute;right:10px;top:40px;font-size:7px;font-weight:600;color:var(--ink)}
.headline{position:absolute;left:29px;top:52px;font-weight:800;line-height:1;font-size:35px;letter-spacing:-.3px}
.headline .l1{color:var(--orange)}
.headline .l2{color:var(--ink);margin-top:3px;display:block}
.headline .l3{display:block;font-size:15px;font-weight:700;margin-top:8px}
.intro{position:absolute;left:0;width:400px;top:348px;text-align:center}
.intro h2{font-size:15px;font-weight:700}
.intro h2 span{color:var(--orange)}
.intro p{font-size:7.4px;line-height:1.4;margin:6px auto 0;width:340px;color:#444}
.services{position:absolute;left:23px;top:404px;width:354px;display:grid;grid-template-columns:repeat(5,54px);grid-template-rows:40px 57px;column-gap:21px;row-gap:30px}
.service{text-align:center;font-size:7.2px;font-weight:500;color:#333;line-height:1.35;border-bottom:1px solid var(--line);display:flex;flex-direction:column;align-items:center;white-space:nowrap}
.service svg{width:20px;height:20px;margin-bottom:5px;flex:none}

/* footer */
.contact-bar{position:absolute;left:0;bottom:0;width:400px;height:23px;background:var(--dark);display:flex;align-items:center}
.contact-bar__label{color:#fff;font-size:11px;font-weight:500;margin-left:45px}
.contact-bar__band{position:absolute;right:0;top:0;height:23px;width:275px;background:var(--orange);clip-path:polygon(0 0,100% 0,100% 100%,22px 100%);display:flex;align-items:center;justify-content:flex-end;padding-right:14px;color:#fff;font-size:7.2px;font-weight:600}

/* back */
.workshop-photo{position:absolute;left:0;top:0;width:400px;height:232px;
  background:linear-gradient(180deg,#b9bdc2 0%,#8e949b 40%,#cfd2d5 75%,rgba(247,247,247,1) 100%)}
.section-title{position:absolute;left:0;width:400px;top:205px;text-align:center;font-family:"Barlow Condensed",sans-serif;line-height:.95}
.section-title .small{display:block;font-weight:300;font-size:26px;letter-spacing:1px;color:var(--ink)}
.section-title .big{display:block;font-weight:700;font-size:40px;color:var(--orange)}
.section-lead{position:absolute;left:0;width:400px;top:276px;text-align:center;font-size:7.8px;line-height:1.4;color:#333}
.service-grid{position:absolute;left:30px;top:304px;width:340px;display:grid;grid-template-columns:1fr 1fr;grid-auto-rows:39px;column-gap:9px;row-gap:5px}
.service-card{background:var(--dark);padding:4px 6px;overflow:hidden}
.service-card h3{color:var(--orange);font-size:7px;font-weight:600;margin-bottom:3px}
.service-card p{color:#c9c9c9;font-size:4.6px;line-height:1.45}
.new-service{position:absolute;left:30px;width:340px;top:523px;text-align:center;font-size:8px;font-weight:700;color:var(--ink)}
.new-service span{color:var(--orange)}
</style>
</head>
<body>

<section class="flyer flyer--front">
  <div class="hero-photo" role="img" aria-label="Verschneite Berglandschaft im Hintergrund"></div>
  <div class="accent-block"></div>
  <div class="tyre-photo" role="img" aria-label="Zwei Reifen mit Alufelgen"></div>
  <div class="brand"><span class="brand__dot"></span>VORLAND REIFEN</div>
  <p class="booking-note">Jetzt Online-Termin buchen</p>
  <h1 class="headline"><span class="l1">REIFEN- UND</span><span class="l2">AUTOSERVICE</span><span class="l3">FÜR IHR FAHRZEUG</span></h1>
  <div class="intro">
    <h2>Wartung und Pflege für IhrE <span>Räder und Reifen</span></h2>
    <p>Der Reifen stellt den Kontakt zwischen Fahrzeug und Fahrbahn her und überträgt alle vom Fahrzeug über das Rad eingeleiteten Kräfte und Momente.</p>
  </div>
  <svg width="0" height="0" style="position:absolute">
    <defs>
      <symbol id="tyre-icon" viewBox="0 0 20 20">
        <rect x="2" y="1.5" width="11" height="17" rx="5" fill="none" stroke="#f19d2a" stroke-width="1.4"/>
        <circle cx="12" cy="10" r="6.5" fill="#fff" stroke="#f19d2a" stroke-width="1.4"/>
        <path d="M12 5.5v9M8 10h8M9 7l6 6M15 7l-6 6" stroke="#f19d2a" stroke-width="1"/>
      </symbol>
    </defs>
  </svg>
  <div class="services">
    <div class="service"><svg><use href="#tyre-icon"/></svg>Winterreifen</div>
    <div class="service"><svg><use href="#tyre-icon"/></svg>Rädereinlagerung</div>
    <div class="service"><svg><use href="#tyre-icon"/></svg>Reifenmontage</div>
    <div class="service"><svg><use href="#tyre-icon"/></svg>Auswuchten</div>
    <div class="service"><svg><use href="#tyre-icon"/></svg>Reifencheck</div>
    <div class="service"><svg><use href="#tyre-icon"/></svg>Reifenreparatur</div>
    <div class="service"><svg><use href="#tyre-icon"/></svg>Luftdruckkontrolle</div>
    <div class="service"><svg><use href="#tyre-icon"/></svg>Kalibrierung des<br>Reifendruckkontroll<br>systems</div>
    <div class="service"><svg><use href="#tyre-icon"/></svg>Räderwäsche</div>
    <div class="service"><svg><use href="#tyre-icon"/></svg>Saisonaler Räder-/<br>Reifenwechsel</div>
  </div>
  <footer class="contact-bar">
    <span class="contact-bar__label">Kontakt</span>
    <div class="contact-bar__band">www.vorland-reifen.de | 04531 555 01 00 | info@vorland-reifen.de</div>
  </footer>
</section>

<section class="flyer flyer--back">
  <div class="workshop-photo" role="img" aria-label="Mechaniker arbeitet am Motorraum eines Autos in der Werkstatt"></div>
  <h1 class="section-title"><span class="small">UNSER</span><span class="big">KFZ-SERVICE</span></h1>
  <p class="section-lead">Unsere Meisterwerkstatt punktet nicht nur mit modernster Ausstattung,<br>sondern auch mit kompetenten Mitarbeitern.</p>
  <div class="service-grid">
    <article class="service-card"><h3>Inspektion</h3><p>Wir führen sämtliche Wartungsarbeiten nach Herstellervorgabe durch und tragen diese in das digitale Serviceheft ein.</p></article>
    <article class="service-card"><h3>Ölservice</h3><p>Wir tauschen das Öl und ggf. den Ölfilter. Wir verwenden ausschließlich Öl mit der jeweiligen Herstellerfreigabe.</p></article>
    <article class="service-card"><h3>Klimaservice</h3><p>Mit unserem hoch modernen Klimaservicegerät überprüfen und befüllen wir Ihr Klimaanlagensystem.</p></article>
    <article class="service-card"><h3>Fehlerdiagnose</h3><p>Mit modernster Diagnosetechnik, die durch ständige Updates auf dem neusten Stand gehalten wird, gehen wir bei der Fehlerdiagnose der Ursache nach.</p></article>
    <article class="service-card"><h3>Stossdämpfer-Service</h3><p>Wir überprüfen Ihre Stoßdämpfer auf ihre Funktionalität und tauschen diese ggf. aus.</p></article>
    <article class="service-card"><h3>Fahrzeugreparaturservice</h3><p>Wir führen Reparatur- und Instandsetzungsarbeiten durch, an folgenden Bauteilen</p></article>
    <article class="service-card"><h3>BatTerieservice</h3><p>Wir laden, prüfen oder erneuern Ihre Batterie. Beim Ausfall der Batterie können wir einen Vor-Ort-Starthilfeservice anbieten.</p></article>
    <article class="service-card"><h3>Wintercheck</h3><p>Wenn die Temperaturen sinken und es anfängt zu frieren ist es Zeit auf Winterreifen umzurüsten.</p></article>
    <article class="service-card"><h3>Bremsenservice</h3><p>Damit das Zusammenspiel Ihrer Bremsanlage in jeder Situation optimal funkHoniert, überprüfen wir diese auf Ihre Funktionalität und stellen diese ggf. wieder her.</p></article>
    <article class="service-card"><h3>Hauptuntersuchung/ Abgasuntersuchung</h3><p>Vorbereitung und Vorführung zur Abnahme der Fahrzeughaupt- und Abgasuntersuchung.</p></article>
  </div>
  <p class="new-service"><span>NEU:</span> LKW- und Landwirtschafts-Reifenservice</p>
  <footer class="contact-bar">
    <span class="contact-bar__label">Kontakt</span>
    <div class="contact-bar__band">www.vorland-reifen.de | 04531 555 01 00 | info@vorland-reifen.de</div>
  </footer>
</section>

</body>
</html>
```